REDESIGN COUPLE PAGES FOR VIMLO VIDEO ADS

PLEASE REDESIGN THIS PAGE FOR ME:
http://pageframequarry.com/kq/rudy/vimlo/pricing.html
I need it to be easy to read for the end user so the customer knows exactly what he will be getting. Make an emphasis on the subscription as the most popular item....and also the price per video format should be emphasized too.

Target Market(s)

B2B

Industry/Entity Type

Video Production

Number of Pages Required

3 page

Colors

Designer to choose colors to be used in the design.

Requirements
Must have
• PLEASE REDESIGN THIS PAGE FOR ME:
• http://pageframequarry.com/kq/rudy/vimlo/pricing.html
• I need it to be easy to read for the end user so the customer knows exactly what he will be getting. Make an emphasis on the subscription as the most popular item....and also the price per video format should be emphasized too.
Nice to have
Should not have

```html
<!DOCTYPE html>
<html lang="en">
<head>
<meta charset="utf-8">
<title>VIMLO Pricing Plans</title>
<link href="https://fonts.googleapis.com/css2?family=Lato:ital,wght@0,400;0,700;0,900;1,700&display=swap" rel="stylesheet">
<style>
:root{
  --navy:#141a2b;
  --ink:#1d2231;
  --muted:#555b66;
  --line:#e5e7eb;
  --stripe:rgba(20,30,60,.045);
  --hero-a:#2353d0;
  --hero-b:#4cabee;
  --blue:#1aa3e8;
  --deep:#1a2d8a;
  --orange:#f3683a;
  --violet:#5a4bc9;
  --red:#e8132b;
  --green:#27b04a;
  --cross:#e4202e;
  --highlight:#f0f2f6;
}
*{box-sizing:border-box;margin:0;padding:0}
html,body{width:893px;height:1200px;overflow:hidden}
body{font-family:'Lato',sans-serif;color:var(--ink);background:#fff;position:relative}
.topbar{position:absolute;left:0;top:0;width:893px;height:36px;background:var(--navy);color:#fff}
.brand{position:absolute;left:131px;top:8px;display:flex;align-items:center;gap:4px}
.brand-mark{width:9px;height:9px;background:#3aa0e8}
.brand-name{font-weight:900;font-size:13px;letter-spacing:1.5px;color:#fff;line-height:1}
.brand-tag{position:absolute;left:131px;top:23px;font-size:4.3px;font-weight:700;letter-spacing:.5px;color:#cfd6e2}
.nav{position:absolute;left:327px;top:13px;display:flex;gap:11px;font-size:7.3px}
.nav a{color:#fff;text-decoration:none}
.nav a.active{color:#4aa8ec}
.login{position:absolute;left:701px;top:14px;font-size:7.3px}
.signup{position:absolute;left:730px;top:9px;width:39px;height:18px;background:#2f7de0;border-radius:2px;font-size:7px;display:flex;align-items:center;justify-content:center}
.hero{position:absolute;left:0;top:36px;width:893px;height:219px;background:linear-gradient(100deg,var(--hero-a) 0%,#3479dc 55%,var(--hero-b) 100%);color:#fff;text-align:center}
.hero h1{position:absolute;top:40px;width:100%;font-size:31px;font-weight:700}
.hero p{position:absolute;top:88px;width:100%;font-size:19px;font-weight:700;font-style:italic}
.plans{position:absolute;left:92px;top:182px;width:710px;height:744px;background:#fff;box-shadow:0 3px 14px rgba(0,0,0,.12)}
.featured-col{position:absolute;left:265px;top:0;width:111px;height:744px;background:var(--highlight);box-shadow:0 3px 10px rgba(0,0,0,.12)}
.divider{position:absolute;top:0;width:1px;height:744px;background:var(--line)}
.grid{position:absolute;left:0;width:710px;display:grid;grid-template-columns:153px 112px 111px 112px 112px 110px}
.head{top:0;height:164px}
.features-title{font-weight:900;font-size:9px;padding:79px 0 0 16px}
.plan{text-align:center;position:relative}
.plan svg{position:absolute;left:50%;top:26px;transform:translateX(-50%)}
.plan-name{position:absolute;top:62px;width:100%;font-weight:700;font-size:8px;line-height:9px}
.plan-sub{position:absolute;top:75px;width:100%;font-size:7px;color:var(--muted);line-height:9px;padding:0 12px}
.plan.tall .plan-sub{top:84px;padding:0 17px}
.price{position:absolute;top:113px;width:100%;font-size:19.5px;font-weight:900}
.price-unit{position:absolute;top:139px;width:100%;font-size:7.5px;font-weight:700}
.rows{top:164px}
.row{display:contents}
.row>div{height:21px;display:flex;align-items:center;justify-content:center;font-size:6.6px;text-transform:uppercase}
.row>div:first-child{justify-content:flex-start;padding-left:16px}
.row.alt>div{background:var(--stripe)}
.tick,.cross{width:7px;height:7px}
.buy-area{top:584px;height:160px}
.buy-cell{position:relative}
.qty{position:absolute;left:19px;top:4px;display:flex}
.qty span{width:20px;height:13px;border:1px solid var(--line);background:#fff;font-size:7px;display:flex;align-items:center;justify-content:center}
.summary{position:absolute;left:0;top:21px;width:100%}
.summary div{height:21px;display:flex;justify-content:space-between;align-items:center;padding:0 9px 0 11px;font-size:6.6px}
.summary div:nth-child(even){background:var(--stripe)}
.summary .grand{font-weight:900}
.btn{position:absolute;left:50%;transform:translateX(-50%);width:63px;height:20px;border:1.3px solid var(--ink);border-radius:10px;font-size:7.5px;font-weight:700;display:flex;align-items:center;justify-content:center;background:#fff}
.btn.primary{background:var(--blue);border-color:var(--blue);color:#fff}
.btn.low{top:121px}
.btn.high{top:11px}
.footer{position:absolute;left:0;top:986px;width:893px;height:214px;background:var(--navy);border-top:2px solid #1fa0e6;color:#fff}
.f-brand{position:absolute;left:192px;top:42px;display:flex;align-items:center;gap:5px}
.f-brand .brand-mark{width:13px;height:13px}
.f-brand .brand-name{font-size:21px;letter-spacing:3px}
.f-tagline{position:absolute;left:192px;top:67px;font-size:6.6px;letter-spacing:1px;color:#d8dde6}
.f-claim{position:absolute;left:192px;top:83px;font-size:9px;font-weight:900}
.f-col h3{font-size:8.8px;font-weight:400}
.f-col h3::after{content:"";display:block;width:12px;height:1px;background:#7a8090;margin-top:6px}
.quick{position:absolute;left:413px;top:44px}
.quick ul{list-style:none;margin-top:8px;font-size:6.8px;line-height:15.5px}
.about{position:absolute;left:546px;top:44px;width:170px}
.about p{margin-top:8px;font-size:7.8px;line-height:12px}
.socials{display:flex;gap:7px;margin-top:10px}
.socials span{width:17px;height:17px;border-radius:50%;background:#222a3d}
.f-rule{position:absolute;left:189px;top:165px;width:517px;height:1px;background:#262d40}
.copyright{position:absolute;top:181px;width:100%;text-align:center;font-size:7.8px}
</style>
</head>
<body>
<header class="topbar">
  <div class="brand"><span class="brand-mark"></span><span class="brand-name">VIMLO</span></div>
  <div class="brand-tag">MARKETING VIDEOS MADE FOR YOU</div>
  <nav class="nav"><a>Home</a><a>How It Works</a><a>Examples</a><a>FAQ</a><a>Contact Us</a><a class="active">Pricing</a><a>Calendar</a></nav>
  <div class="login">Log In</div>
  <div class="signup">Sign Up</div>
</header>

<section class="hero">
  <h1>Pricing Plans</h1>
  <p>No Hidden Charges! Choose Your DEAL!</p>
</section>

<svg width="0" height="0" style="position:absolute">
  <defs>
    <symbol id="tick" viewBox="0 0 10 10"><circle cx="5" cy="5" r="5" fill="#27b04a"/><path d="M2.8 5.2l1.5 1.5 3-3" fill="none" stroke="#fff" stroke-width="1.3" stroke-linecap="round" stroke-linejoin="round"/></symbol>
    <symbol id="cross" viewBox="0 0 10 10"><circle cx="5" cy="5" r="5" fill="#e4202e"/><path d="M3.5 3.5l3 3M6.5 3.5l-3 3" stroke="#fff" stroke-width="1.2" stroke-linecap="round"/></symbol>
  </defs>
</svg>

<main class="plans">
  <div class="featured-col"></div>
  <div class="divider" style="left:153px"></div>
  <div class="divider" style="left:376px"></div>
  <div class="divider" style="left:488px"></div>
  <div class="divider" style="left:600px"></div>

  <div class="grid head">
    <div class="features-title">FEATURES</div>
    <div class="plan">
      <svg width="28" height="28" viewBox="0 0 28 28" fill="none" stroke="#1a2d8a" stroke-width="1.5" stroke-linejoin="round"><path d="M2 6l8-3 8 3 8-3v19l-8 3-8-3-8 3z"/><path d="M10 3v19M18 6v19"/></svg>
      <div class="plan-name">AL A CARTE</div><div class="plan-sub">As Needed Basis</div>
      <div class="price" style="color:var(--deep)">$37.00</div><div class="price-unit">Video Format</div>
    </div>
    <div class="plan">
      <svg width="28" height="28" viewBox="0 0 28 28" fill="none" stroke="#1aa3e8" stroke-width="1.5" stroke-linejoin="round"><rect x="3" y="3" width="22" height="16" rx="3"/><path d="M6 7l8 6 8-6M6 16l5-4M22 16l-5-4"/><path d="M12 17v7h5v-4"/></svg>
      <div class="plan-name">SUBSCRIPTION</div><div class="plan-sub">New Video Ads Monthly</div>
      <div class="price" style="color:var(--blue)">$16.00</div><div class="price-unit">Video Format</div>
    </div>
    <div class="plan">
      <svg width="30" height="28" viewBox="0 0 30 28" fill="none" stroke="#f3683a" stroke-width="1.5" stroke-linecap="round"><path d="M5 11c4-7 14-8 20-3z" fill="#f3683a"/><path d="M15 8l-4 14M3 22c3 0 3 2 6 2s3-2 6-2M3 26c3 0 3-1.5 6-1.5M17 22h10"/></svg>
      <div class="plan-name">HOLIDAY PKG</div><div class="plan-sub">17 Holiday Themed Videos</div>
      <div class="price" style="color:var(--orange)">$14.00</div><div class="price-unit">Video Format</div>
    </div>
    <div class="plan">
      <svg width="28" height="30" viewBox="0 0 28 30" fill="none" stroke="#5a4bc9" stroke-width="1.4" stroke-linejoin="round"><path d="M9 2L3 24h12zM20 7l-5 17h10zM9 24v5M20 24v5M2 29h24"/></svg>
      <div class="plan-name">SEASON PKG</div><div class="plan-sub">4 Seasonal Themed Videos</div>
      <div class="price" style="color:var(--violet)">$18.00</div><div class="price-unit">Video Format</div>
    </div>
    <div class="plan tall">
      <svg width="26" height="26" viewBox="0 0 26 26" fill="none" stroke="#e8132b" stroke-width="1.5"><rect x="2" y="4" width="22" height="20" rx="2"/><path d="M2 10h22M8 1v6M18 1v6"/><path d="M7 14h2M12 14h2M17 14h2M7 18h2M12 18h2M17 18h2" stroke-width="2"/></svg>
      <div class="plan-name">SOCIAL MEDIA<br>CALENDAR</div><div class="plan-sub">Daily Videos For Your Social Media</div>
      <div class="price" style="color:var(--red)">$18.00</div><div class="price-unit">Video Format</div>
    </div>
  </div>

  <div class="grid rows">
    <div class="row alt"><div>Videos included</div><div>Custom</div><div>Custom</div><div>17</div><div>4</div><div>4</div></div>
    <div class="row"><div>Cost per video format</div><div>Starts @ $37/video</div><div>Starts @ $16/video</div><div>$14/video</div><div>$18/video</div><div>$18/video</div></div>
    <div class="row alt"><div>Delivery speed</div><div>24 hours</div><div>24 hours</div><div>3-5 days</div><div>3-5 days</div><div>3-5 days</div></div>
    <div class="row"><div>Revisions</div><div>Unlimited</div><div>Unlimited</div><div>Unlimited</div><div>Unlimited</div><div>Unlimited</div></div>
    <div class="row alt"><div>Final file formats</div><div>MP4 Full HD 1080P</div><div>MP4 Full HD 1080P</div><div>MP4 Full HD 1080P</div><div>MP4</div><div>MP4 Full HD 1080P</div></div>
    <div class="row"><div>Wide screen video format</div><div><svg class="tick"><use href="#tick"/></svg></div><div><svg class="tick"><use href="#tick"/></svg></div><div><svg class="tick"><use href="#tick"/></svg></div><div><svg class="tick"><use href="#tick"/></svg></div><div><svg class="tick"><use href="#tick"/></svg></div></div>
    <div class="row alt"><div>Large square video format</div><div><svg class="tick"><use href="#tick"/></svg></div><div><svg class="tick"><use href="#tick"/></svg></div><div><svg class="tick"><use href="#tick"/></svg></div><div><svg class="tick"><use href="#tick"/></svg></div><div><svg class="tick"><use href="#tick"/></svg></div></div>
    <div class="row"><div>Vertical video format</div><div><svg class="tick"><use href="#tick"/></svg></div><div><svg class="tick"><use href="#tick"/></svg></div><div><svg class="tick"><use href="#tick"/></svg></div><div><svg class="tick"><use href="#tick"/></svg></div><div><svg class="tick"><use href="#tick"/></svg></div></div>
    <div class="row alt"><div>Page cover video format</div><div><svg class="tick"><use href="#tick"/></svg></div><div><svg class="tick"><use href="#tick"/></svg></div><div><svg class="tick"><use href="#tick"/></svg></div><div><svg class="tick"><use href="#tick"/></svg></div><div><svg class="tick"><use href="#tick"/></svg></div></div>
    <div class="row"><div>Holiday theme video</div><div>Optional</div><div><svg class="tick"><use href="#tick"/></svg></div><div><svg class="tick"><use href="#tick"/></svg></div><div><svg class="cross"><use href="#cross"/></svg></div><div><svg class="cross"><use href="#cross"/></svg></div></div>
    <div class="row alt"><div>Seasonal theme video</div><div>Optional</div><div><svg class="tick"><use href="#tick"/></svg></div><div><svg class="cross"><use href="#cross"/></svg></div><div><svg class="tick"><use href="#tick"/></svg></div><div><svg class="tick"><use href="#tick"/></svg></div></div>
    <div class="row"><div>Content done for you</div><div><svg class="tick"><use href="#tick"/></svg></div><div><svg class="tick"><use href="#tick"/></svg></div><div><svg class="tick"><use href="#tick"/></svg></div><div><svg class="tick"><use href="#tick"/></svg></div><div><svg class="tick"><use href="#tick"/></svg></div></div>
    <div class="row alt"><div>Full branding in video</div><div><svg class="tick"><use href="#tick"/></svg></div><div><svg class="tick"><use href="#tick"/></svg></div><div><svg class="tick"><use href="#tick"/></svg></div><div><svg class="tick"><use href="#tick"/></svg></div><div><svg class="tick"><use href="#tick"/></svg></div></div>
    <div class="row"><div>Full copyright ownership</div><div><svg class="tick"><use href="#tick"/></svg></div><div><svg class="tick"><use href="#tick"/></svg></div><div><svg class="tick"><use href="#tick"/></svg></div><div><svg class="tick"><use href="#tick"/></svg></div><div><svg class="tick"><use href="#tick"/></svg></div></div>
    <div class="row alt"><div>Full reselling rights</div><div><svg class="tick"><use href="#tick"/></svg></div><div><svg class="tick"><use href="#tick"/></svg></div><div><svg class="tick"><use href="#tick"/></svg></div><div><svg class="tick"><use href="#tick"/></svg></div><div><svg class="tick"><use href="#tick"/></svg></div></div>
    <div class="row"><div>Premium video clips</div><div><svg class="tick"><use href="#tick"/></svg></div><div><svg class="tick"><use href="#tick"/></svg></div><div><svg class="tick"><use href="#tick"/></svg></div><div><svg class="tick"><use href="#tick"/></svg></div><div><svg class="tick"><use href="#tick"/></svg></div></div>
    <div class="row alt"><div>Use my images</div><div><svg class="tick"><use href="#tick"/></svg></div><div><svg class="tick"><use href="#tick"/></svg></div><div><svg class="tick"><use href="#tick"/></svg></div><div><svg class="tick"><use href="#tick"/></svg></div><div><svg class="tick"><use href="#tick"/></svg></div></div>
    <div class="row"><div>Use my video footage</div><div><svg class="tick"><use href="#tick"/></svg></div><div><svg class="tick"><use href="#tick"/></svg></div><div><svg class="tick"><use href="#tick"/></svg></div><div><svg class="tick"><use href="#tick"/></svg></div><div><svg class="tick"><use href="#tick"/></svg></div></div>
    <div class="row alt"><div>Use my background music</div><div><svg class="tick"><use href="#tick"/></svg></div><div><svg class="tick"><use href="#tick"/></svg></div><div><svg class="tick"><use href="#tick"/></svg></div><div><svg class="tick"><use href="#tick"/></svg></div><div><svg class="tick"><use href="#tick"/></svg></div></div>
    <div class="row"><div>Fully licensed background music</div><div><svg class="tick"><use href="#tick"/></svg></div><div><svg class="tick"><use href="#tick"/></svg></div><div><svg class="tick"><use href="#tick"/></svg></div><div><svg class="tick"><use href="#tick"/></svg></div><div><svg class="tick"><use href="#tick"/></svg></div></div>
  </div>

  <div class="grid buy-area">
    <div></div>
    <div class="buy-cell">
      <div class="qty"><span>-</span><span>1</span><span>+</span></div>
      <div class="summary">
        <div><span>TOTAL</span><span>$149</span></div>
        <div><span>DISCOUNT</span><span>$29.80</span></div>
        <div><span>PRICE PER VIDEO</span><span>$119.20</span></div>
        <div class="grand"><span>GRAND TOTAL</span><span>$119.20</span></div>
      </div>
      <div class="btn low">BUY NOW</div>
    </div>
    <div class="buy-cell">
      <div class="qty"><span>-</span><span>1</span><span>+</span></div>
      <div class="summary">
        <div><span>TOTAL</span><span>$99</span></div>
        <div><span>DISCOUNT</span><span>$19.80</span></div>
        <div><span>PRICE PER VIDEO</span><span>$79.20</span></div>
        <div class="grand"><span>GRAND TOTAL</span><span>$79.20</span></div>
      </div>
      <div class="btn low primary">BUY NOW</div>
    </div>
    <div class="buy-cell"><div class="btn high">BUY NOW</div></div>
    <div class="buy-cell"><div class="btn high">BUY NOW</div></div>
    <div class="buy-cell"><div class="btn high">BUY NOW</div></div>
  </div>
</main>

<footer class="footer">
  <div class="f-brand"><span class="brand-mark"></span><span class="brand-name">VIMLO</span></div>
  <div class="f-tagline">MARKETING VIDEOS MADE FOR YOU</div>
  <div class="f-claim">CREATED BY A MARKETER FOR MARKETERS.</div>
  <div class="f-col quick">
    <h3>Quick Links</h3>
    <ul><li>How It Works</li><li>Term Of Service</li><li>Privacy Policy</li><li>Cookies Policy</li></ul>
  </div>
  <div class="f-col about">
    <h3>About Us</h3>
    <p>With Vimlo, you simply let us know what you want to promote and we will have your video ad finished as soon as 24 hours!</p>
    <div class="socials"><span></span><span></span><span></span><span></span><span></span></div>
  </div>
  <div class="f-rule"></div>
  <div class="copyright">©2019 All Rights Reserved | Privacy Statement. Site Map</div>
</footer>
</body>
</html>
```